k eLiquid Label

We are an electronic cigarette eLiquid manufacturer with an outdated label design which needs to be updated and become more modern. All information listed on the label cannot be changed or removed.

There are 4 colour coding on the labels that cannot change.
0mg is white
12mg is yellow
18mg is blue
24mg is red

We prefer a blue type background however are not committed to it with the proper design however if a new colour is chosen it must compliment the colour band for each colour coding

The "dots" on the front of the bottle need to be larger.

The "V" on the front needs to be in this font however we can accept slight changes to it for effect.

Issues we are facing:
The 0mg and the 18mg look too close in colour and need to be completely different in colouring.

The background colouring is too dark and you cannot see the 50/50 in the watermark.

Reason: We have not received a design which is suitable to our needs. We have see a few close ones however not exact. Thanks

Reason: I was forced to go out of country for a family emergency and to be fair I am extending the deadline

```html
<!DOCTYPE html>
<html lang="en">
<head>
<meta charset="utf-8">
<title>k eLiquid Label – Sweet Tobacco Range</title>
<link rel="stylesheet" href="https://fonts.googleapis.com/css2?family=Roboto:wght@400;500;700&family=Roboto+Condensed:wght@400;700&display=swap">
<style>
  :root {
    --page: #ffffff;
    --label-blue-light: #3a8fd6;
    --label-blue: #2a74c0;
    --label-blue-deep: #1d5ea9;
    --watermark: rgba(120, 205, 255, 0.32);
    --ink-light: #ffffff;
    --ink-dark: #2b2b2b;
    --band-zero: #ffffff;
    --band-twelve: #f4d21c;
    --band-eighteen: #3a3d98;
    --band-twentyfour: #c7282f;
  }

  * { box-sizing: border-box; margin: 0; padding: 0; }

  html, body {
    width: 1200px;
    height: 738px;
    overflow: hidden;
    background: var(--page);
  }

  .range {
    position: relative;
    width: 1200px;
    height: 738px;
    display: flex;
    justify-content: center;
    align-items: center;
    gap: 72px;
    padding-bottom: 40px;
  }

  .label {
    position: relative;
    width: 176px;
    height: 240px;
    display: flex;
    flex-direction: column;
    overflow: hidden;
    background: linear-gradient(90deg, var(--label-blue-deep) 0%, var(--label-blue-light) 45%, var(--label-blue) 100%);
    font-family: "Roboto", Arial, sans-serif;
  }

  .band {
    height: 18px;
    flex: none;
    display: flex;
    justify-content: space-around;
    align-items: center;
    font-family: "Roboto Condensed", "Arial Narrow", sans-serif;
    font-weight: 700;
    font-size: 9px;
    letter-spacing: 0.3px;
    white-space: nowrap;
    background: var(--band);
    color: var(--band-ink);
    position: relative;
    z-index: 2;
  }

  .label--zero { --band: var(--band-zero); --band-ink: var(--ink-dark); --dot-ink: var(--label-blue); }
  .label--twelve { --band: var(--band-twelve); --band-ink: var(--ink-dark); --dot-ink: var(--ink-dark); }
  .label--eighteen { --band: var(--band-eighteen); --band-ink: var(--ink-light); --dot-ink: var(--ink-light); }
  .label--twentyfour { --band: var(--band-twentyfour); --band-ink: var(--ink-light); --dot-ink: var(--ink-light); }

  .panel {
    position: relative;
    flex: 1;
  }

  .watermark {
    position: absolute;
    top: 4px;
    right: -10px;
    font-family: "Roboto", Arial, sans-serif;
    font-weight: 400;
    font-size: 40px;
    line-height: 38px;
    color: var(--watermark);
    text-align: right;
    white-space: nowrap;
  }

  .brand {
    position: absolute;
    left: 12px;
    right: 8px;
    top: 78px;
    display: flex;
    align-items: center;
    gap: 6px;
  }

  .strength-dot {
    width: 30px;
    height: 30px;
    flex: none;
    border-radius: 50%;
    background: var(--band);
    color: var(--dot-ink);
    display: flex;
    align-items: center;
    justify-content: center;
    font-size: 15px;
    font-weight: 400;
  }

  .label--zero .strength-dot { font-size: 12px; }

  .brand-name {
    color: var(--ink-light);
    font-size: 26px;
    font-weight: 400;
    line-height: 1;
    white-space: nowrap;
  }

  .volume {
    position: absolute;
    right: 10px;
    top: 112px;
    color: var(--ink-light);
    font-size: 8px;
  }

  .flavour {
    position: absolute;
    left: 0;
    right: 0;
    bottom: 8px;
    text-align: center;
    color: var(--ink-light);
    font-family: "Roboto Condensed", "Arial Narrow", sans-serif;
    font-weight: 400;
    font-size: 20px;
    letter-spacing: -0.3px;
  }
</style>
</head>
<body>
<main class="range">

  <article class="label label--zero">
    <div class="band"><span>FREE</span><span>NICOTINE</span><span>FREE</span><span>NICOTINE</span></div>
    <div class="panel">
      <div class="watermark" aria-hidden="true">50/50<br>50/50<br>50/50<br>50/50<br>50/50</div>
      <div class="brand"><span class="strength-dot">zero</span><span class="brand-name">k eLiquid</span></div>
      <span class="volume">30 ml</span>
      <p class="flavour">SWEET TOBACCO</p>
    </div>
    <div class="band"><span>NICOTINE</span><span>ZÉRO</span><span>NICOTINE</span><span>ZÉRO</span></div>
  </article>

  <article class="label label--twelve">
    <div class="band"><span>12 mg/ml</span><span>12 mg/ml</span><span>12 mg/ml</span></div>
    <div class="panel">
      <div class="watermark" aria-hidden="true">50/50<br>50/50<br>50/50<br>50/50<br>50/50</div>
      <div class="brand"><span class="strength-dot">12</span><span class="brand-name">k eLiquid</span></div>
      <span class="volume">30 ml</span>
      <p class="flavour">SWEET TOBACCO</p>
    </div>
    <div class="band"><span>POISON</span><span>DANGER</span><span>POISON</span></div>
  </article>

  <article class="label label--eighteen">
    <div class="band"><span>18 mg/ml</span><span>18 mg/ml</span><span>18 mg/ml</span></div>
    <div class="panel">
      <div class="watermark" aria-hidden="true">50/50<br>50/50<br>50/50<br>50/50<br>50/50</div>
      <div class="brand"><span class="strength-dot">18</span><span class="brand-name">k eLiquid</span></div>
      <span class="volume">30 ml</span>
      <p class="flavour">SWEET TOBACCO</p>
    </div>
    <div class="band"><span>POISON</span><span>DANGER</span><span>POISON</span></div>
  </article>

  <article class="label label--twentyfour">
    <div class="band"><span>24 mg/ml</span><span>24 mg/ml</span><span>24 mg/ml</span></div>
    <div class="panel">
      <div class="watermark" aria-hidden="true">50/50<br>50/50<br>50/50<br>50/50<br>50/50</div>
      <div class="brand"><span class="strength-dot">24</span><span class="brand-name">k eLiquid</span></div>
      <span class="volume">30 ml</span>
      <p class="flavour">SWEET TOBACCO</p>
    </div>
    <div class="band"><span>POISON</span><span>DANGER</span><span>POISON</span></div>
  </article>

</main>
</body>
</html>
```